EXPEDITE PROJECT: New business cards and stationery
New start up
Brisk,looks good so far.. card #9 would be the one I would pick so far.
Can you Pls add - (Human Capital Experts) on the front of the card.
Back -Let us bring creative strategic HR innovation experience and expertise to your organization.
Tks,
Carlow

```html
<!DOCTYPE html>
<html lang="en">
<head>
<meta charset="utf-8">
<title>Northvale Stationery Set</title>
<link href="https://fonts.googleapis.com/css2?family=Open+Sans:wght@400;600&display=swap" rel="stylesheet">
<style>
  :root {
    --stage: #2b2b2e;
    --paper: #ffffff;
    --blue: #1f63c6;
    --blue-deep: #0d3f95;
    --orange: #e8862a;
    --ink: #4a4f5a;
    --ink-soft: #8a909c;
    --ghost: #eef1f6;
  }
  * { box-sizing: border-box; margin: 0; padding: 0; }
  html, body { width: 1200px; height: 701px; overflow: hidden; background: var(--stage); }
  body { position: relative; font-family: "Open Sans", Arial, sans-serif; color: var(--ink); }
  .piece { position: absolute; background: var(--paper); overflow: hidden; box-shadow: 0 3px 10px rgba(0,0,0,.45); }
  .header-band { position: absolute; left: 0; top: 0; width: 100%; }
  .brand { position: absolute; display: flex; align-items: center; gap: 6px; }
  .brand-dot { border-radius: 50%; background: var(--orange); flex: none; }
  .brand-name { font-weight: 600; color: var(--blue-deep); letter-spacing: .04em; text-transform: uppercase; line-height: 1; }
  .tagline { position: absolute; color: var(--blue-deep); white-space: nowrap; }
  .contact-list { position: absolute; list-style: none; color: var(--ink-soft); }
  .contact-list li { display: flex; align-items: center; gap: 4px; white-space: nowrap; }
  .contact-icon { width: 5px; height: 5px; background: var(--blue); border-radius: 1px; flex: none; }
  .ghost-circle { position: absolute; border-radius: 50%; background: var(--ghost); }

  /* business card front */
  .card-front { left: 137px; top: 41px; width: 199px; height: 103px; }
  .card-front .holder { position: absolute; right: 10px; top: 3px; text-align: right; color: #fff; line-height: 1.2; }
  .card-front .holder-name { font-size: 7px; font-weight: 600; }
  .card-front .holder-role { font-size: 4.5px; opacity: .9; }
  .card-front .brand { left: 8px; top: 44px; gap: 4px; }
  .card-front .brand-dot { width: 12px; height: 12px; }
  .card-front .brand-name { font-size: 6.5px; }
  .card-front .tagline { left: 8px; top: 62px; font-size: 4.5px; }
  .card-front .contact-list { left: 98px; top: 58px; font-size: 4.2px; line-height: 6.5px; }

  /* business card back */
  .card-back { left: 348px; top: 41px; width: 194px; height: 103px; }
  .card-back .message { position: absolute; left: 0; right: 0; top: 10px; text-align: center; font-size: 5px; line-height: 7px; color: var(--ink); padding: 0 28px; }
  .card-back .brand-dot { position: absolute; left: 82px; top: 32px; width: 30px; height: 30px; }
  .card-back .web { position: absolute; left: 0; right: 0; bottom: 14px; text-align: center; font-size: 5px; color: var(--blue); }

  /* envelope back */
  .envelope-back { left: 89px; top: 178px; width: 453px; height: 206px; }
  .envelope-back svg { position: absolute; inset: 0; }
  .envelope-back .seal { position: absolute; left: 218px; top: 8px; width: 17px; height: 17px; border-radius: 50%; background: var(--orange); }

  /* envelope front */
  .envelope-front { left: 89px; top: 413px; width: 453px; height: 211px; }
  .envelope-front .brand { left: 12px; top: 56px; }
  .envelope-front .brand-dot { width: 28px; height: 28px; }
  .envelope-front .brand-name { font-size: 12px; }
  .envelope-front .tagline { left: 46px; top: 88px; font-size: 7px; }
  .envelope-front .return-address { position: absolute; left: 12px; top: 110px; font-size: 5px; color: var(--ink-soft); }
  .envelope-front .ghost-circle { left: 338px; top: 90px; width: 96px; height: 96px; }

  /* letterhead */
  .letterhead { left: 672px; top: 43px; width: 432px; height: 619px; }
  .letterhead .brand { left: 16px; top: 48px; }
  .letterhead .brand-dot { width: 30px; height: 30px; }
  .letterhead .brand-name { font-size: 13px; }
  .letterhead .tagline { left: 52px; top: 84px; font-size: 7px; }
  .letterhead .ghost-circle { left: 136px; top: 236px; width: 160px; height: 160px; }
  .letterhead .return-address { position: absolute; right: 86px; bottom: 20px; font-size: 4.5px; line-height: 6.5px; color: var(--ink-soft); text-align: right; }
  .letterhead .contact-list { right: 12px; bottom: 20px; font-size: 4.5px; line-height: 6.5px; }
</style>
</head>
<body>

<svg width="0" height="0" style="position:absolute" aria-hidden="true">
  <defs>
    <linearGradient id="band-fill" x1="0" y1="0" x2="1" y2="0">
      <stop offset="0" stop-color="#0d3f95"/>
      <stop offset="1" stop-color="#2a78dc"/>
    </linearGradient>
  </defs>
</svg>

<section class="piece card-front" aria-label="Business card, front">
  <svg class="header-band" viewBox="0 0 199 44" preserveAspectRatio="none" height="44">
    <path d="M0 0H199V26C140 26 70 30 0 38Z" fill="url(#band-fill)"/>
    <path d="M0 41C70 33 140 29 199 29" fill="none" stroke="var(--orange)" stroke-width="1.4"/>
  </svg>
  <div class="holder">
    <p class="holder-name">Carlow Ambers</p>
    <p class="holder-role">Managing Director</p>
  </div>
  <div class="brand"><span class="brand-dot"></span><span class="brand-name">Northvale</span></div>
  <p class="tagline">Human Capital Experts</p>
  <ul class="contact-list">
    <li><span class="contact-icon"></span>301 555 0142</li>
    <li><span class="contact-icon"></span>301 555 0143</li>
    <li><span class="contact-icon"></span>301 555 0144</li>
    <li><span class="contact-icon"></span>carlow@northvalehr.com</li>
    <li><span class="contact-icon"></span>www.northvalehr.com</li>
  </ul>
</section>

<section class="piece card-back" aria-label="Business card, back">
  <p class="message">Let us bring creative strategic HR innovation experience and expertise to your organization.</p>
  <span class="brand-dot"></span>
  <p class="web">www.northvalehr.com</p>
</section>

<section class="piece envelope-back" aria-label="Envelope, back">
  <svg viewBox="0 0 453 206" preserveAspectRatio="none">
    <path d="M0 0L226 62L453 0" fill="none" stroke="#dfe2e8" stroke-width="1.2"/>
  </svg>
  <span class="seal"></span>
</section>

<section class="piece envelope-front" aria-label="Envelope, front">
  <svg class="header-band" viewBox="0 0 453 70" preserveAspectRatio="none" height="70">
    <path d="M0 0H453V40C330 24 150 20 0 50Z" fill="url(#band-fill)"/>
    <path d="M170 34C300 28 400 40 453 50" fill="none" stroke="var(--orange)" stroke-width="3"/>
    <path d="M250 40C340 40 410 52 453 62" fill="none" stroke="#5a3a1a" stroke-width="2"/>
  </svg>
  <div class="brand"><span class="brand-dot"></span><span class="brand-name">Northvale</span></div>
  <p class="tagline">Human Capital Experts</p>
  <p class="return-address">100 Central Pkwy, Northvale, MD 20601</p>
  <span class="ghost-circle"></span>
</section>

<section class="piece letterhead" aria-label="Letterhead">
  <svg class="header-band" viewBox="0 0 432 70" preserveAspectRatio="none" height="70">
    <path d="M0 0H432V16C300 22 130 36 0 64Z" fill="url(#band-fill)"/>
    <path d="M110 46C220 26 340 18 432 18" fill="none" stroke="var(--orange)" stroke-width="2.6"/>
  </svg>
  <div class="brand"><span class="brand-dot"></span><span class="brand-name">Northvale</span></div>
  <p class="tagline">Human Capital Experts</p>
  <span class="ghost-circle"></span>
  <p class="return-address">100 Central Pkwy<br>Suite 210<br>Northvale, MD 20601</p>
  <ul class="contact-list">
    <li><span class="contact-icon"></span>301 555 0142</li>
    <li><span class="contact-icon"></span>301 555 0143</li>
    <li><span class="contact-icon"></span>info@northvalehr.com</li>
    <li><span class="contact-icon"></span>www.northvalehr.com</li>
  </ul>
</section>

</body>
</html>
```